Creative Real Estate Listing Mailer

I would like a creative double sided Real Estate listing flier/mailer to send out enticing people to list their house for sale with me. An example in my head, but feel free to be creative,.. would be one side with a Weiner dog with a sack of money on its back saying something like " its time to cash in" and the other side having some kind of southwest backdrop ( I live in Arizona) or luxury home, with my photo and my contact info saying something like list your house with me, or see what your home is worth etc.

Target Market(s)

People interested in selling their homes

Industry/Entity Type

Real Estate Agent

Contact Information for Business Card

Similar to the flyer, but simpler

Requirements
Must have
• My name: Milo Trask
My Email: milotrask@brevlo.com
My Phone# (480) 555 0147
Website www.Milotrask.com

```html
<!DOCTYPE html>
<html lang="en">
<head>
<meta charset="utf-8">
<title>Saguaro Crest Realty – Listing Mailer</title>
<link rel="stylesheet" href="https://fonts.googleapis.com/css2?family=Anton&family=Montserrat:wght@300;500;600;700&display=swap">
<style>
  :root {
    --stage: #5f5f5f;
    --paper: #ffffff;
    --paper-grey: #e9e9e9;
    --royal: #24479b;
    --maroon: #6b0d14;
    --orange: #d77e16;
    --orange-light: #e6a23a;
    --ink: #1d1d2b;
    --rule: #b9b9b9;
  }
  * { box-sizing: border-box; margin: 0; padding: 0; }
  html, body { width: 900px; height: 1200px; overflow: hidden; }
  body { background: var(--stage); font-family: "Montserrat", sans-serif; position: relative; }

  .card { position: absolute; width: 674px; height: 482px; overflow: hidden; background: var(--paper); }
  .card--front { left: 113px; top: 86px; background: linear-gradient(135deg, #f4f4f4 0%, #ececec 55%, #dcdcdc 100%); }
  .card--back { left: 112px; top: 632px; }
  .card__art { position: absolute; inset: 0; width: 100%; height: 100%; }

  .brand { position: absolute; display: flex; align-items: center; gap: 8px; color: var(--ink); font-weight: 600; }
  .brand__mark { background: var(--maroon); flex: none; }
  .brand__name { line-height: 1.05; letter-spacing: 0.06em; text-transform: uppercase; }
  .card--front .brand { left: 46px; top: 40px; }
  .card--front .brand__mark { width: 46px; height: 46px; }
  .card--front .brand__name { font-size: 21px; }
  .card--back .brand { left: 380px; top: 40px; }
  .card--back .brand__mark { width: 26px; height: 26px; }
  .card--back .brand__name { font-size: 12px; }

  .headline { position: absolute; left: 44px; top: 136px; font-family: "Anton", sans-serif; color: #fff; line-height: 0.98; text-shadow: 0 2px 3px rgba(0,0,0,.25); }
  .headline__top { display: block; font-size: 62px; letter-spacing: 0.01em; }
  .headline__big { display: block; font-size: 84px; letter-spacing: 0.01em; }

  .ribbon { position: absolute; left: 40px; top: 302px; width: 289px; height: 50px; border-radius: 0 0 8px 8px;
    background: linear-gradient(180deg, var(--orange-light), var(--orange)); color: #fff;
    font-family: "Anton", sans-serif; font-size: 29px; display: flex; align-items: center; justify-content: center; letter-spacing: 0.01em; }

  .hero-photo { position: absolute; left: 334px; top: 34px; width: 324px; height: 342px; border-radius: 10px;
    background: radial-gradient(ellipse at 40% 55%, #3a2a1e 0%, #5b4330 45%, #c9b08a 80%, rgba(220,205,180,0) 100%); }

  .social { position: absolute; left: 575px; top: 323px; width: 110px; height: 38px; border-radius: 19px 0 0 19px;
    background: var(--maroon); display: flex; align-items: center; gap: 7px; padding-left: 10px; }
  .social__dot { width: 23px; height: 23px; border-radius: 50%; background: var(--royal); }
  .social__dot--light { background: #3a9be6; }

  .call { position: absolute; left: 46px; top: 393px; color: #fff; }
  .call__line { font-size: 30px; font-weight: 700; letter-spacing: 0.02em; line-height: 1; }
  .call__lead { color: var(--orange-light); font-weight: 300; }
  .call__phone { display: flex; align-items: center; gap: 9px; margin-top: 11px; font-size: 37px; font-weight: 600; line-height: 1; }
  .phone-badge { width: 37px; height: 37px; flex: none; }

  .badge { position: absolute; }
  .badge--house { left: 466px; top: 418px; width: 44px; height: 44px; }
  .badge--listing { left: 532px; top: 418px; width: 102px; height: 48px; border: 3px solid #1b2a8f; background: #fff; }

  .pitch { position: absolute; left: 36px; top: 27px; width: 270px; font-size: 19.5px; font-weight: 700; line-height: 1.26; color: #111; }
  .pitch__house { color: var(--maroon); }
  .pitch__home { color: var(--royal); }

  .agent-photo { position: absolute; left: 68px; top: 88px; width: 210px; height: 250px; border-radius: 100px 100px 0 0;
    background: linear-gradient(180deg, #c7b2a6 0%, #a38c80 40%, #1f2d55 70%, #1a2648 100%); }

  .agent-name { position: absolute; left: 67px; top: 340px; font-size: 24px; font-weight: 700; color: #fff; letter-spacing: 0.02em; }
  .contact { position: absolute; left: 40px; top: 383px; color: #fff; list-style: none; }
  .contact__item { display: flex; align-items: center; gap: 10px; line-height: 1; }
  .contact__item + .contact__item { margin-top: 8px; }
  .contact__icon { width: 15px; height: 15px; flex: none; }
  .contact__item--mail { font-size: 16px; font-weight: 500; }
  .contact__item--phone { font-size: 23px; font-weight: 600; }
  .contact__item--web { font-size: 16px; font-weight: 600; }

  .stamp-box { position: absolute; left: 559px; top: 39px; width: 75px; height: 84px; border: 1px solid #8a8a8a; }
  .address-line { position: absolute; left: 455px; width: 179px; height: 0; border-top: 1px solid var(--rule); }
</style>
</head>
<body>

<section class="card card--front" aria-label="Mailer front">
  <svg class="card__art" viewBox="0 0 674 482" preserveAspectRatio="none" aria-hidden="true">
    <rect class="band-blue" x="0" y="126" width="385" height="185" fill="#24479b"/>
    <rect x="0" y="404" width="674" height="78" fill="#ffffff"/>
    <polygon points="352,374 366,374 452,476 674,476 674,482 0,482" fill="#24479b"/>
    <polygon points="0,374 350,374 436,482 0,482" fill="#6b0d14"/>
    <rect x="0" y="477" width="674" height="5" fill="#6b0d14"/>
  </svg>

  <div class="brand">
    <span class="brand__mark"></span>
    <span class="brand__name">Saguaro Crest<br>Realty</span>
  </div>

  <h1 class="headline">
    <span class="headline__top">ITS TIME TO</span>
    <span class="headline__big">CASH IN</span>
  </h1>
  <div class="ribbon">LIST YOUR HOUSE NOW</div>

  <div class="hero-photo" role="img" aria-label="Photo of a dachshund sitting beside a burlap money sack and stacks of cash"></div>

  <div class="social" aria-label="Social links">
    <span class="social__dot"></span>
    <span class="social__dot social__dot--light"></span>
  </div>

  <div class="call">
    <p class="call__line"><span class="call__lead">CALL</span> MILO TRASK</p>
    <p class="call__phone">
      <svg class="phone-badge" viewBox="0 0 40 40" aria-hidden="true">
        <circle cx="20" cy="20" r="18" fill="#24479b" stroke="#fff" stroke-width="3"/>
        <path d="M14 11c2-1 3 0 4 3l-2 2c1 3 3 5 6 6l2-2c3 1 4 2 3 4l-2 2c-7 0-13-6-13-13z" fill="#fff"/>
      </svg>
      (480) 555 0147
    </p>
  </div>

  <svg class="badge badge--house" viewBox="0 0 44 44" aria-hidden="true">
    <rect x="4" y="4" width="36" height="36" fill="#111"/>
  </svg>
  <div class="badge badge--listing" aria-hidden="true"></div>
</section>

<section class="card card--back" aria-label="Mailer back">
  <svg class="card__art" viewBox="0 0 674 482" preserveAspectRatio="none" aria-hidden="true">
    <defs>
      <linearGradient id="dusk" x1="0" y1="0" x2="0" y2="1">
        <stop offset="0" stop-color="#e6c3d6"/>
        <stop offset="0.35" stop-color="#f3d2bf"/>
        <stop offset="0.7" stop-color="#b9a6a2"/>
        <stop offset="1" stop-color="#9d8f86"/>
      </linearGradient>
    </defs>
    <polygon points="0,0 280,0 366,241 280,482 0,482" fill="url(#dusk)"/>
    <polygon points="290,0 317,0 401,241 317,482 290,482 375,241" fill="#24479b"/>
    <polygon points="0,338 257,338 245,376 0,376" fill="#24479b"/>
    <polygon points="0,376 245,376 257,338 337,338 285,482 0,482" fill="#6b0d14"/>
  </svg>

  <p class="pitch">List <span class="pitch__house">Your House</span> with me, or see what <span class="pitch__home">Your Home</span> is worth.</p>

  <div class="agent-photo" role="img" aria-label="Portrait of the agent in a navy suit in front of a desert city skyline at dusk"></div>

  <p class="agent-name">MILO TRASK</p>
  <ul class="contact">
    <li class="contact__item contact__item--mail">
      <svg class="contact__icon" viewBox="0 0 16 16" aria-hidden="true"><rect x="1" y="3" width="14" height="10" fill="none" stroke="#fff" stroke-width="1.3"/><path d="M1 3l7 6 7-6" fill="none" stroke="#fff" stroke-width="1.3"/></svg>
      milotrask@brevlo.com
    </li>
    <li class="contact__item contact__item--phone">
      <svg class="contact__icon" viewBox="0 0 16 16" aria-hidden="true"><circle cx="8" cy="8" r="7" fill="none" stroke="#fff" stroke-width="1.3"/><path d="M5.5 4.5c1-.5 1.5 0 2 1.5l-1 1c.5 1.5 1.5 2.5 3 3l1-1c1.5.5 2 1 1.5 2l-1 1c-3.5 0-6.5-3-6.5-6.5z" fill="#fff"/></svg>
      (480) 555 0147
    </li>
    <li class="contact__item contact__item--web">
      <svg class="contact__icon" viewBox="0 0 16 16" aria-hidden="true"><circle cx="8" cy="8" r="7" fill="none" stroke="#fff" stroke-width="1.3"/><ellipse cx="8" cy="8" rx="3" ry="7" fill="none" stroke="#fff" stroke-width="1.1"/><path d="M1 8h14" stroke="#fff" stroke-width="1.1"/></svg>
      www.Milotrask.com
    </li>
  </ul>

  <div class="brand">
    <span class="brand__mark"></span>
    <span class="brand__name">Saguaro Crest<br>Realty</span>
  </div>

  <div class="stamp-box" aria-hidden="true"></div>
  <div class="address-line" style="top:284px"></div>
  <div class="address-line" style="top:327px"></div>
  <div class="address-line" style="top:370px"></div>
</section>

</body>
</html>
```